Kelvara Constructions Business card and Logo

We are a building company that would like our current logo design copied with the "Kelvara Constructions" lines thicker.
We would also like our business cards copied with some minor copy changes. I have attached images of our logo and business cards.
We would like a standard size business card in landscape format rather than portrait.
On the back of the business card we would like a name added above the mobile number - "Teodor Marsk"
Can I please get high res file of the logo and business cards at completion of redesign?

```html
<!DOCTYPE html>
<html lang="en">
<head>
<meta charset="utf-8">
<title>Kelvara Constructions – Business Card</title>
<link rel="stylesheet" href="https://fonts.googleapis.com/css2?family=Lato:wght@300;400;700;900&display=swap">
<style>
  :root {
    --page-bg: #e6e6e3;
    --green-light: #3f9e45;
    --green-mid: #2f8a37;
    --green-dark: #1f6a28;
    --card-black: #0b0b0b;
    --ink-white: #ffffff;
    --ink-soft: rgba(255, 255, 255, 0.88);
    --shadow: 0 14px 30px rgba(0, 0, 0, 0.22);
  }
  * { box-sizing: border-box; margin: 0; padding: 0; }
  html, body {
    width: 1200px;
    height: 873px;
    overflow: hidden;
    background: var(--page-bg);
    font-family: "Lato", Arial, sans-serif;
  }
  .sheet {
    width: 1200px;
    height: 873px;
    display: flex;
    align-items: center;
    justify-content: center;
    gap: 60px;
  }
  .card {
    position: relative;
    width: 500px;
    height: 286px;
    border-radius: 3px;
    overflow: hidden;
    box-shadow: var(--shadow);
    color: var(--ink-white);
  }
  /* Front: contact side */
  .card--front .card__pattern {
    position: absolute;
    inset: 0;
    background: linear-gradient(135deg, var(--green-light) 0%, var(--green-mid) 50%, var(--green-dark) 100%);
  }
  .card__content {
    position: absolute;
    left: 150px;
    top: 46px;
    right: 30px;
  }
  .brand-name {
    font-weight: 900;
    font-size: 21px;
    letter-spacing: 0.2px;
    color: var(--ink-white);
    display: flex;
    align-items: center;
    gap: 8px;
  }
  .brand-name__dot {
    width: 7px;
    height: 7px;
    background: var(--ink-white);
    border-radius: 50%;
  }
  .contact__name {
    margin-top: 26px;
    font-weight: 400;
    font-size: 19px;
  }
  .contact__line {
    margin-top: 6px;
    font-weight: 300;
    font-size: 13.5px;
    color: var(--ink-soft);
    letter-spacing: 0.2px;
  }
  .contact__line .sep { margin: 0 6px; }
  .contact__web {
    margin-top: 22px;
    font-weight: 400;
    font-size: 13.5px;
  }
  /* Back: brand side */
  .card--back {
    background: var(--card-black);
    display: flex;
    align-items: center;
    justify-content: center;
  }
  .card--back .brand-name {
    font-size: 28px;
    flex-direction: column;
    gap: 0;
    line-height: 1.15;
    text-align: center;
  }
</style>
</head>
<body>
  <main class="sheet">
    <section class="card card--front" aria-label="Business card front">
      <div class="card__pattern" role="img" aria-label="Green geometric chevron pattern background"></div>
      <div class="card__content">
        <div class="brand-name">Kelvara Constructions<span class="brand-name__dot"></span></div>
        <p class="contact__name">Teodor Marsk</p>
        <p class="contact__line">e-mail: hello@kelvara.au</p>
        <p class="contact__line">Ph: 0400 512 209<span class="sep">/</span>Fax: 03 9000 4417</p>
        <p class="contact__line">PO Box 114 Carrow, Vic 3990</p>
        <p class="contact__web">kelvara.net.au</p>
      </div>
    </section>

    <section class="card card--back" aria-label="Business card back">
      <div class="brand-name">
        <span>Kelvara</span>
        <span>Constructions</span>
      </div>
    </section>
  </main>
</body>
</html>
```